Computer company startup need wordpress template

I am looking for a new design that is fresh, bold and stands out from the crowd for an IT company called Torvane Computers. We specialise in consumer and small business IT.

It will have to be mobile friendly, viewable on all devices. I need a template that i can work with and that will give our site a professional look and feel but not look like every other site out there.

To see what text will be on final site, see www.torvanecomputers-demo.com.au, i will change wording, but it is pretty close to what it's meant to be.

I have supplied logo and the main colours on car, business cards etc is black, red (and shades thereof) and white.

I am visualiing some home page with "Welcome to Torvane Computers, how may we help you today?" then 4 cool looking buttons below which says:

1. Residential computer / network issues
2. Business computer / network issues
3. Home Networking
4. New home networking

These buttons will then take you to the correct page which i will flesh out from the template. All pages need have sections for my support links etc.

Website built from template will have 5-6 pages max.

If anyone need any additional direction, please send me a message and i will answer.

Target Market(s)

Consumer and small business (1-20 employees) customers

Industry/Entity Type

It Company

Requirements
Must have
• professional look and feel

```html
<!DOCTYPE html>
<html lang="en">
<head>
<meta charset="utf-8">
<title>Torvane Computers</title>
<link href="https://fonts.googleapis.com/css2?family=Open+Sans:wght@400;600;700;800&display=swap" rel="stylesheet">
<style>
:root{
  --red:#d7141d;
  --red-dark:#a80f16;
  --ink:#2b2b2b;
  --muted:#777;
  --light:#f0f0f0;
  --line:#dcdcdc;
  --footer:#262626;
  --footer-deep:#161616;
  --white:#fff;
}
*{box-sizing:border-box;margin:0;padding:0}
html,body{width:706px;height:1200px;overflow:hidden;background:#fff}
body{font-family:"Open Sans",Arial,sans-serif;color:var(--ink)}
.page{width:706px;height:1200px;position:relative;overflow:hidden}

/* header */
.site-header{height:80px;position:relative;background:var(--white)}
.brand{position:absolute;left:28px;top:18px;display:flex;align-items:center;gap:8px}
.brand-dot{width:16px;height:16px;border-radius:50%;background:var(--red)}
.brand-name{font-weight:800;font-size:24px;color:var(--red);letter-spacing:-.5px}
.top-bar{position:absolute;right:28px;top:12px;display:flex;align-items:center;gap:8px}
.top-bar .phone{display:flex;align-items:center;gap:5px;font-size:12px;font-weight:600;color:var(--ink);margin-right:6px}
.pill{background:var(--red);color:#fff;font-size:10px;font-weight:600;padding:4px 10px;border-radius:3px}
.main-nav{position:absolute;right:28px;bottom:0;display:flex}
.main-nav a{font-size:11px;font-weight:700;color:var(--ink);text-decoration:none;padding:8px 14px;border-left:1px solid var(--line)}
.main-nav a:first-child{border-left:0}
.main-nav a.active{background:var(--red);color:#fff;border-radius:4px 4px 0 0}

/* hero */
.hero{height:270px;position:relative;background:linear-gradient(180deg,#5d6a78 0%,#a3b2c2 45%,#dfe6ee 100%)}
.hero-caption{position:absolute;right:24px;bottom:24px;background:rgba(20,20,20,.85);color:#fff;font-weight:700;font-size:18px;line-height:1.25;padding:12px 18px;width:262px}

/* welcome */
.welcome{height:180px;text-align:center;padding-top:22px}
.welcome h1{font-size:23px;font-weight:700;display:flex;align-items:center;justify-content:center;gap:8px}
.welcome h1 .brand-name{font-size:24px}
.rule{width:50px;height:2px;background:var(--red);margin:8px auto 12px}
.welcome p{font-size:10px;line-height:1.6;color:var(--muted);width:560px;margin:0 auto}
.btn{display:inline-block;background:var(--red);color:#fff;font-size:10px;font-weight:600;padding:6px 16px;border-radius:2px;margin-top:12px}

/* services */
.services{height:250px;background:var(--light);text-align:center;padding-top:18px}
.section-title{font-size:18px;font-weight:800;text-transform:uppercase}
.section-title span{color:var(--red)}
.swoosh{display:block;margin:2px auto 14px}
.service-grid{display:flex;justify-content:center;gap:22px}
.service{width:146px}
.service-icon{width:72px;height:72px;border-radius:50%;border:3px solid var(--red);background:#fff;margin:0 auto 8px;display:flex;align-items:center;justify-content:center}
.service h3{font-size:12px;font-weight:700;line-height:1.3;min-height:32px}
.service p{font-size:8.5px;line-height:1.5;color:var(--muted);margin-top:4px;min-height:26px}
.service .more{font-size:9px;color:var(--red);font-weight:600;margin-top:4px;display:block}

/* testimonial */
.testimonial{height:160px;padding-top:18px;text-align:center}
.quote-block{display:flex;align-items:center;gap:20px;width:620px;margin:0 auto;text-align:left}
.client-photo{width:76px;height:76px;border-radius:50%;flex:none;background:linear-gradient(135deg,#c9a58a,#e7d6c9);border:3px solid #fff;box-shadow:0 0 0 1px var(--line)}
.quote-mark{font-size:40px;color:#c8c8c8;font-weight:800;line-height:1;align-self:flex-start}
.quote-block p{font-size:9.5px;line-height:1.6;color:var(--muted)}

/* partners */
.partners{height:60px;background:var(--light);display:flex;align-items:center;justify-content:space-between;padding:0 14px}
.arrow{width:20px;height:20px;border-radius:50%;background:var(--red);display:flex;align-items:center;justify-content:center;flex:none}
.partner-list{display:flex;justify-content:space-around;flex:1}
.partner-list span{font-size:15px;font-weight:700;color:#555}

/* footer */
.site-footer{height:176px;background:var(--footer);color:#ccc;display:flex;gap:20px;padding:18px 26px 0}
.site-footer h4{color:#fff;font-size:12px;font-weight:700;margin-bottom:10px;white-space:nowrap}
.col-links{width:100px}
.col-links li{list-style:none;font-size:9.5px;line-height:1.9}
.col-links li::before{content:"› ";color:var(--red)}
.col-news{width:170px;font-size:9px;line-height:1.5}
.field{background:#fff;color:#999;font-size:9px;padding:5px 8px;margin-top:8px;display:flex;align-items:center;gap:5px}
.subscribe{display:inline-block;background:var(--red);color:#fff;font-size:9px;font-weight:700;padding:5px 12px;margin-top:6px}
.col-contact{width:196px;font-size:9px;line-height:1.7}
.col-contact .row{display:flex;gap:6px;align-items:center;white-space:nowrap}
.col-contact .row svg{flex:none}
.col-contact strong{color:#fff}
.col-social{flex:1}
.col-social .row{display:flex;align-items:center;gap:8px;font-size:9.5px;margin-bottom:8px}
.col-social .sq{width:14px;height:14px;background:#555;border-radius:2px}
.bottom-bar{height:24px;background:var(--footer-deep);display:flex;justify-content:space-between;align-items:center;padding:0 26px;font-size:8.5px}
.bottom-bar .copy{color:var(--red)}
.bottom-bar .legal{color:#aaa}
</style>
</head>
<body>
<div class="page">

<header class="site-header">
  <div class="brand"><span class="brand-dot"></span><span class="brand-name">Torvane Computers</span></div>
  <div class="top-bar">
    <span class="phone">
      <svg width="12" height="12" viewBox="0 0 24 24"><path fill="#d7141d" d="M6.6 10.8a15 15 0 0 0 6.6 6.6l2.2-2.2c.3-.3.7-.4 1-.2 1.1.4 2.3.6 3.6.6.6 0 1 .4 1 1V20c0 .6-.4 1-1 1A17 17 0 0 1 3 4c0-.6.4-1 1-1h3.5c.6 0 1 .4 1 1 0 1.3.2 2.5.6 3.6.1.3 0 .7-.2 1z"/></svg>
      555-014-2290
    </span>
    <span class="pill">New user</span>
    <span class="pill">Sign In</span>
  </div>
  <nav class="main-nav">
    <a class="active" href="#">Home</a><a href="#">About Us</a><a href="#">Services</a><a href="#">Contact Us</a><a href="#">FAQs</a>
  </nav>
</header>

<section class="hero" role="img" aria-label="Photo of a businessman holding a tablet with floating devices and network icons">
  <div class="hero-caption">We specialise in consumer and small business IT</div>
</section>

<section class="welcome">
  <h1>Welcome To <span class="brand-name">Torvane Computers</span></h1>
  <div class="rule"></div>
  <p>We keep homes and small offices running with friendly, fast and honest computer support. From new machines and data backups to network setup and security, our local technicians handle it all so you can get on with your day. Talk to us about repairs, upgrades or ongoing care plans built for your needs.</p>
  <span class="btn">Read More</span>
</section>

<section class="services">
  <h2 class="section-title">Our <span>Services</span></h2>
  <svg class="swoosh" width="90" height="8" viewBox="0 0 90 8"><path d="M2 6 Q45 -2 88 6" stroke="#d7141d" stroke-width="2" fill="none"/></svg>
  <div class="service-grid">
    <div class="service">
      <div class="service-icon"><svg width="32" height="32" viewBox="0 0 24 24"><path fill="none" stroke="#d7141d" stroke-width="2" stroke-linecap="round" d="M4 20 14 10M15 4a5 5 0 0 0 5 5M4 4l6 6M17 14l3 6M14 17l6 3"/></svg></div>
      <h3>Custom Built Computers</h3>
      <p>Desktops built to your spec for gaming, study or office work.</p>
      <span class="more">Read More »</span>
    </div>
    <div class="service">
      <div class="service-icon"><svg width="32" height="32" viewBox="0 0 24 24" fill="none" stroke="#d7141d" stroke-width="2"><ellipse cx="12" cy="5" rx="8" ry="3"/><path d="M4 5v14c0 1.7 3.6 3 8 3s8-1.3 8-3V5M4 12c0 1.7 3.6 3 8 3s8-1.3 8-3"/></svg></div>
      <h3>Data Backup And Recovery</h3>
      <p>Automatic backups and careful recovery when drives fail.</p>
      <span class="more">Read More »</span>
    </div>
    <div class="service">
      <div class="service-icon"><svg width="32" height="32" viewBox="0 0 24 24" fill="none" stroke="#d7141d" stroke-width="2"><rect x="9" y="2" width="6" height="5"/><rect x="2" y="17" width="6" height="5"/><rect x="16" y="17" width="6" height="5"/><path d="M12 7v5M5 17v-5h14v5"/></svg></div>
      <h3>Computer And Network IT Security</h3>
      <p>Secure wired and wireless networks for homes and small offices.</p>
      <span class="more">Read More »</span>
    </div>
    <div class="service">
      <div class="service-icon"><svg width="32" height="32" viewBox="0 0 24 24" fill="none" stroke="#d7141d" stroke-width="2"><circle cx="12" cy="12" r="9"/><ellipse cx="12" cy="12" rx="4" ry="9"/><path d="M3 12h18"/></svg></div>
      <h3>Internet Installations And Advice</h3>
      <p>Clean, tidy installs plus honest advice on the right equipment.</p>
      <span class="more">Read More »</span>
    </div>
  </div>
</section>

<section class="testimonial">
  <h2 class="section-title">Client <span>Testimonial</span></h2>
  <svg class="swoosh" width="90" height="8" viewBox="0 0 90 8"><path d="M2 6 Q45 -2 88 6" stroke="#d7141d" stroke-width="2" fill="none"/></svg>
  <div class="quote-block">
    <div class="client-photo" role="img" aria-label="Portrait photo of a satisfied client"></div>
    <span class="quote-mark">“</span>
    <p>Torvane Computers sorted out our office network in a single afternoon. The team explained every step, set up backups for all six machines and left everything labelled and tidy. We have not had a single outage since, and their follow-up support has been quick, patient and genuinely helpful.</p>
  </div>
</section>

<section class="partners">
  <span class="arrow"><svg width="10" height="10" viewBox="0 0 10 10"><path d="M7 1 3 5l4 4" stroke="#fff" stroke-width="2" fill="none"/></svg></span>
  <div class="partner-list">
    <span>Corvex</span><span>Halden</span><span>Nuvora</span><span>Brightcore</span><span>Altamo</span><span>Kestrel</span>
  </div>
  <span class="arrow"><svg width="10" height="10" viewBox="0 0 10 10"><path d="M3 1l4 4-4 4" stroke="#fff" stroke-width="2" fill="none"/></svg></span>
</section>

<footer class="site-footer">
  <div class="col-links">
    <h4>Quick Links</h4>
    <ul><li>Home</li><li>About Us</li><li>Services</li><li>Contact Us</li><li>FAQs</li></ul>
  </div>
  <div class="col-news">
    <h4>Newsletter Sign Up</h4>
    <p>Stay updated with latest news from Torvane Computers support team.</p>
    <div class="field"><svg width="10" height="8" viewBox="0 0 10 8"><rect x=".5" y=".5" width="9" height="7" fill="none" stroke="#999"/><path d="M.5.5 5 4.5 9.5.5" fill="none" stroke="#999"/></svg>Enter Your Email</div>
    <span class="subscribe">SUBSCRIBE</span>
  </div>
  <div class="col-contact">
    <h4>Contact Information</h4>
    <div class="row"><strong>Torvane Computers</strong></div>
    <div class="row"><svg width="9" height="11" viewBox="0 0 10 12"><path d="M5 0a4 4 0 0 0-4 4c0 3 4 8 4 8s4-5 4-8a4 4 0 0 0-4-4z" fill="#d7141d"/></svg>Unit 4, 18 Harbour Street, Kellerton</div>
    <div class="row"><svg width="10" height="10" viewBox="0 0 24 24"><path fill="#d7141d" d="M6.6 10.8a15 15 0 0 0 6.6 6.6l2.2-2.2c.3-.3.7-.4 1-.2 1.1.4 2.3.6 3.6.6.6 0 1 .4 1 1V20c0 .6-.4 1-1 1A17 17 0 0 1 3 4c0-.6.4-1 1-1h3.5c.6 0 1 .4 1 1 0 1.3.2 2.5.6 3.6.1.3 0 .7-.2 1z"/></svg>(03) 9555 0142</div>
    <div class="row"><svg width="10" height="10" viewBox="0 0 10 10"><rect x="1" y="1" width="8" height="8" fill="none" stroke="#d7141d"/></svg>(03) 9555 0143</div>
    <div class="row"><svg width="10" height="8" viewBox="0 0 10 8"><rect x=".5" y=".5" width="9" height="7" fill="none" stroke="#d7141d"/><path d="M.5.5 5 4.5 9.5.5" fill="none" stroke="#d7141d"/></svg>info@torvanecomputers-demo.com.au</div>
  </div>
  <div class="col-social">
    <h4>Follow us</h4>
    <div class="row"><span class="sq"></span>Friendsly</div>
    <div class="row"><span class="sq"></span>Chirper</div>
    <div class="row"><span class="sq"></span>Circlemesh</div>
    <div class="row"><span class="sq"></span>Linkwork</div>
  </div>
</footer>
<div class="bottom-bar">
  <span class="copy">Copyright © 2015 Torvane Computers . All Rights Reserved.</span>
  <span class="legal">Privacy Policy | Terms &amp; Conditions</span>
</div>

</div>
</body>
</html>
```